Flyer design for the Harvest Of Light Summit 2019 (HOLSUM)

Design a flyer for our annual conference with basic information about the conference: conference logo and year, Conference name: Harvest Of Light Summit Location: Tallow Community Center (Downtown Portland)382 Wimbrel Lane, Portland, ME 04107, Date: August 8th, 9th, 10th and 11th, 2019Start time 7:00PMI would like the following three words added to the flyer. These words describe the vision of the conference: Prophetic, Fire, Overflow,

Contact info:
Website: www.quentavo.org
Phone: 207 555 0143
Email: contact@plumvesta.org

Target Market(s)

Young adults living in the United States

Industry/Entity Type

Religious

Font styles to use
Sans Serif

Colors

Designer to choose colors to be used in the design.

Requirements
Must have
• HOLSUM must logo standout, the reader should be able to take a quick look and find key info,
Should not have
• Cross image, church image

```html
<!DOCTYPE html>
<html lang="en">
<head>
<meta charset="utf-8">
<title>HOLSUM 2019 – Harvest Of Light Summit</title>
<link rel="stylesheet" href="https://fonts.googleapis.com/css2?family=Montserrat:wght@700&family=Josefin+Sans:wght@400&family=Lato:wght@400;700;900&family=Oswald:wght@500&family=Marcellus+SC&display=swap">
<style>
  :root {
    --ink-black: #050505;
    --brand-blue: #1a78c2;
    --flame-orange: #f7931e;
    --deep-orange: #ff6a00;
    --navy: #14284f;
    --paper: #ffffff;
    --soft-paper: #f4f2ef;
  }
  * { margin: 0; padding: 0; box-sizing: border-box; }
  html, body { width: 902px; height: 1200px; overflow: hidden; background: var(--soft-paper); }
  .flyer { position: relative; width: 902px; height: 1200px; overflow: hidden; }
  .backdrop { position: absolute; inset: 0; }
  .layer { position: absolute; left: 0; width: 100%; text-align: center; white-space: nowrap; }

  .event-mark {
    top: 82px;
    font-family: "Montserrat", sans-serif; font-weight: 700;
    font-size: 150px; line-height: 1; letter-spacing: 4px;
    color: var(--brand-blue);
  }
  .event-year {
    top: 262px; display: flex; align-items: center; justify-content: center; gap: 22px;
    font-family: "Montserrat", sans-serif; font-weight: 700;
    font-size: 62px; line-height: 1; letter-spacing: 26px; color: var(--flame-orange);
  }
  .event-year .rule { width: 186px; height: 3px; background: var(--flame-orange); }
  .event-year span.num { margin-right: -26px; }
  .event-name {
    top: 346px; line-height: 1;
    font-family: "Josefin Sans", sans-serif; font-weight: 400;
    font-size: 42px; letter-spacing: 0.5px; color: var(--paper);
  }

  .info { left: 290px; width: 584px; }
  .vision {
    top: 586px; line-height: 40px;
    font-family: "Josefin Sans", sans-serif; font-size: 35px; letter-spacing: 0.5px; color: #111;
  }
  .pin { top: 645px; left: calc(290px + 292px - 24px); width: 48px; height: 48px; }
  .venue-name {
    top: 708px; line-height: 28px; font-family: "Lato", sans-serif; font-weight: 900;
    font-size: 24px; color: var(--deep-orange); letter-spacing: 0.3px;
  }
  .venue-address {
    top: 738px; font-family: "Lato", sans-serif; font-size: 22px; line-height: 29px; color: var(--navy);
  }
  .divider {
    display: flex; align-items: center; justify-content: center; gap: 14px; line-height: 24px;
    font-family: "Marcellus SC", sans-serif; font-size: 19px; color: var(--deep-orange);
  }
  .divider .rule { height: 3px; width: 245px; background: linear-gradient(90deg, transparent, var(--navy) 40%, var(--navy)); }
  .divider .rule.right { background: linear-gradient(270deg, transparent, var(--navy) 40%, var(--navy)); width: 225px; }
  .date-divider { top: 812px; left: 270px; width: 632px; }
  .time-divider { top: 918px; left: 270px; width: 632px; }
  .event-dates {
    top: 856px; line-height: 46px; font-family: "Oswald", sans-serif; font-weight: 500;
    font-size: 35px; color: var(--navy); letter-spacing: 0;
  }
  .event-dates .hl { color: var(--deep-orange); }
  .start-time {
    top: 956px; line-height: 34px; font-family: "Marcellus SC", sans-serif; font-size: 28px; color: var(--navy);
  }

  .contacts { position: absolute; left: 140px; top: 1056px; font-family: "Lato", sans-serif; color: var(--paper); font-style: normal; white-space: nowrap; }
  .contact-row { display: flex; align-items: center; gap: 12px; height: 32px; }
  .contact-row svg { width: 22px; height: 22px; flex: none; }
  .contact-row.phone { font-size: 29px; font-weight: 900; height: 40px; }
  .contact-row.email, .contact-row.web { font-size: 21px; font-weight: 700; }
</style>
</head>
<body>
<main class="flyer">
  <svg class="backdrop" viewBox="0 0 902 1200" width="902" height="1200">
    <defs>
      <radialGradient id="emberGlow" cx="0.55" cy="0.75" r="0.7">
        <stop offset="0" stop-color="#3a1608"/>
        <stop offset="0.45" stop-color="#1a0a04"/>
        <stop offset="1" stop-color="#050505"/>
      </radialGradient>
      <radialGradient id="fireGlow" cx="0.15" cy="0.35" r="0.8">
        <stop offset="0" stop-color="#fffbd0"/>
        <stop offset="0.18" stop-color="#ffe44a"/>
        <stop offset="0.45" stop-color="#ffb21c"/>
        <stop offset="0.75" stop-color="#f7a23a"/>
        <stop offset="1" stop-color="#f7a23a" stop-opacity="0"/>
      </radialGradient>
      <linearGradient id="fireFade" x1="0" x2="1">
        <stop offset="0.35" stop-color="#fff" stop-opacity="0"/>
        <stop offset="1" stop-color="#fff" stop-opacity="1"/>
      </linearGradient>
      <linearGradient id="paperShade" x1="0" x2="1" y1="0" y2="1">
        <stop offset="0" stop-color="#ffffff"/>
        <stop offset="1" stop-color="#ebe9e7"/>
      </linearGradient>
    </defs>

    <rect class="dark-field" width="902" height="1200" fill="url(#emberGlow)" role="img" aria-label="Dark smoky backdrop with faint glowing flames"/>

    <path class="paper-wave" fill="url(#paperShade)"
      d="M0 620 C90 600 180 585 250 560 L290 548 L262 590 C330 565 420 540 500 520 L560 480 C600 455 660 420 760 410 C830 405 870 420 902 440 L902 1200 L0 1200 Z"/>

    <g role="img" aria-label="Bright yellow and orange flames rising from the lower left">
      <rect x="0" y="600" width="400" height="470" fill="url(#fireGlow)"/>
      <rect x="0" y="600" width="400" height="470" fill="url(#fireFade)"/>
    </g>

    <path class="flame-band-light" fill="#ff8a2a"
      d="M0 975 C70 950 150 960 200 990 L300 930 L265 1000 C340 1010 410 1040 450 1070 C540 1110 680 1120 780 1110 C840 1105 880 1085 902 1060 L902 1200 L0 1200 Z"/>
    <path class="flame-band" fill="var(--deep-orange)"
      d="M0 1000 C80 985 150 995 215 1015 L330 950 L290 1030 C370 1035 440 1065 480 1090 L440 1085 C520 1120 640 1140 740 1140 C800 1140 860 1120 902 1095 L902 1200 L0 1200 Z"/>
  </svg>

  <h1 class="layer event-mark">HOLSUM</h1>
  <div class="layer event-year"><span class="rule"></span><span class="num">2019</span><span class="rule"></span></div>
  <h2 class="layer event-name">HARVEST OF LIGHT SUMMIT</h2>

  <p class="layer info vision">PROPHETIC, FIRE, OVERFLOW</p>
  <svg class="layer pin" viewBox="0 0 50 50" aria-label="Location">
    <circle cx="25" cy="25" r="23" fill="#fff" stroke="#1a78c2" stroke-width="1.5"/>
    <path d="M25 13 C19.5 13 16 17 16 21.5 C16 27.5 25 37 25 37 C25 37 34 27.5 34 21.5 C34 17 30.5 13 25 13 Z" fill="none" stroke="#f7931e" stroke-width="2.6"/>
    <circle cx="25" cy="21.5" r="3.2" fill="#f7931e"/>
  </svg>
  <p class="layer info venue-name">TALLOW COMMUNITY CENTER</p>
  <p class="layer info venue-address">(Downtown Portland)382 Wimbrel Lane,<br>Portland, ME 04107</p>

  <div class="layer divider date-divider"><span class="rule"></span>Date<span class="rule right"></span></div>
  <p class="layer info event-dates">AUGUST <span class="hl">8TH, 9TH, 10TH AND 11TH,</span> 2019</p>
  <div class="layer divider time-divider"><span class="rule"></span>Start Time<span class="rule right"></span></div>
  <p class="layer info start-time">7:00PM</p>

  <address class="contacts">
    <div class="contact-row phone">
      <svg viewBox="0 0 24 24"><circle cx="12" cy="12" r="10.5" fill="none" stroke="#fff" stroke-width="1.8"/><path d="M8.5 7 L10.5 7 L11.2 9.6 L10 10.6 C10.6 12 11.8 13.3 13.3 14 L14.3 12.8 L16.9 13.5 L16.9 15.5 C12 16 8 12 8.5 7 Z" fill="#fff"/></svg>
      207 555 0143
    </div>
    <div class="contact-row email">
      <svg viewBox="0 0 24 24"><rect x="3" y="6" width="18" height="12" fill="#fff"/><path d="M3 6 L12 13 L21 6" fill="none" stroke="#ff6a00" stroke-width="1.6"/></svg>
      contact@plumvesta.org
    </div>
    <div class="contact-row web">
      <svg viewBox="0 0 24 24" fill="none" stroke="#fff" stroke-width="1.6"><circle cx="12" cy="12" r="9"/><ellipse cx="12" cy="12" rx="4" ry="9"/><path d="M3 12 H21 M5 7.5 H19 M5 16.5 H19"/></svg>
      www.quentavo.org
    </div>
  </address>
</main>
</body>
</html>
```